BRICKWORK BLUEPRINT: THE RELIABLE WAY TO EARN HUGE GAINS FROM BUDGET HOME UPGRADES

I am looking for a book cover design for my new E-Book.

My idea for the design is a pin board with before and after photos of our properties pinned on it (example attached). I have also attached some photos to use.

PLEASE SUBMIT OTHER DESIGNS ALSO AS THIS WAS JUST AN IDEA BUT I AM OPEN TO OTHER IDEAS ALSO.

Page size is 5x7 inches

Font styles to use
Serif
Sans Serif

Colors
0255a3
3176b5
85acd3
85cae6
33a6d7
0392cd
9bcb3c
abd036
ec1f27

```html
<!DOCTYPE html>
<html lang="en">
<head>
<meta charset="utf-8">
<title>Brickwork Blueprint – E-Book Cover</title>
<link href="https://fonts.googleapis.com/css2?family=Anton&family=Rubik+Dirt&family=Oswald:wght@700&family=Kalam:wght@400&family=Marcellus+SC&display=swap" rel="stylesheet">
<style>
  :root{
    --paper:#ece5d8;
    --paper-edge:#d9cfbd;
    --ink:#141414;
    --navy:#1c2642;
    --red:#c8161d;
    --cork:#b4804f;
    --cork-dark:#9a6a3f;
    --frame:#d8c6a2;
    --frame-dark:#b9a57f;
    --polaroid:#fbfbf8;
    --pin-red:#d8262b;
    --pin-blue:#2f5bb5;
    --pin-green:#3e9a46;
    --sky:#7fb2e6;
    --lawn:#5f9a3a;
    --house:#8d96a3;
  }
  *{margin:0;padding:0;box-sizing:border-box}
  html,body{width:800px;height:1200px;overflow:hidden;background:#fff}
  .cover{
    position:relative;width:800px;height:1200px;overflow:hidden;
    background:radial-gradient(ellipse at 50% 45%, #f3eee4 0%, var(--paper) 55%, var(--paper-edge) 100%);
  }
  .title-main{
    position:absolute;left:0;right:0;top:14px;text-align:center;
    font-family:"Anton",sans-serif;font-size:150px;line-height:1;
    color:var(--ink);letter-spacing:6px;
  }
  .title-accent{
    position:absolute;left:0;right:0;top:160px;text-align:center;
    font-family:"Rubik Dirt",sans-serif;font-size:112px;line-height:1;
    color:var(--red);letter-spacing:2px;
  }
  .board{
    position:absolute;left:24px;top:340px;width:752px;height:551px;
    background:linear-gradient(var(--frame),var(--frame-dark));
    padding:11px;box-shadow:0 6px 14px rgba(0,0,0,.35);
  }
  .board-cork{
    width:100%;height:100%;
    background:radial-gradient(ellipse at 50% 40%, var(--cork) 0%, var(--cork-dark) 100%);
    box-shadow:inset 0 0 10px rgba(0,0,0,.45);
  }
  .snap{
    position:absolute;background:var(--polaroid);
    padding:8px 8px 0 8px;box-shadow:2px 4px 8px rgba(0,0,0,.4);
  }
  .snap-photo{
    width:100%;
    background:linear-gradient(180deg,var(--sky) 0%,#b9d4ee 32%,var(--house) 33%,#b7bcc2 60%,var(--lawn) 61%,#4d7f2e 100%);
  }
  .snap-photo.is-before{
    background:linear-gradient(180deg,#c3d3e2 0%,#dfe5ea 30%,#75716c 31%,#9a968f 62%,#6e6a62 63%,#8a8376 100%);
  }
  .snap-label{
    font-family:"Kalam",cursive;font-size:21px;color:#333;
    padding:4px 0 0 14px;line-height:1.2;
  }
  .pin{position:absolute;width:12px;height:12px;border-radius:50%;
    box-shadow:1px 2px 3px rgba(0,0,0,.45)}
  .pin.red{background:var(--pin-red)}
  .pin.blue{background:var(--pin-blue)}
  .pin.green{background:var(--pin-green)}
  .tagline{position:absolute;left:0;right:0;top:920px;text-align:center;
    font-family:"Oswald",sans-serif;font-weight:700;line-height:1}
  .tagline-lead{display:block;font-size:34px;color:var(--navy)}
  .tagline-key{display:block;font-size:54px;color:var(--red);margin-top:2px}
  .tagline-tail{display:block;font-size:36px;color:var(--navy);margin-top:4px}
  .credits{position:absolute;left:0;right:0;top:1104px;text-align:center;
    font-family:"Marcellus SC",serif;font-size:22px;color:var(--navy);
    line-height:1.45;letter-spacing:1px}
</style>
</head>
<body>
<div class="cover">
  <h1>
    <span class="title-main">BRICKWORK</span>
    <span class="title-accent">BLUEPRINT</span>
  </h1>

  <div class="board"><div class="board-cork"></div></div>

  <span class="pin blue" style="left:100px;top:390px"></span>
  <span class="pin red" style="left:160px;top:392px"></span>
  <span class="pin red" style="left:724px;top:634px"></span>
  <span class="pin blue" style="left:728px;top:664px"></span>
  <span class="pin red" style="left:734px;top:692px"></span>

  <figure class="snap" style="left:173px;top:414px;width:168px;height:208px;transform:rotate(7deg)">
    <div class="snap-photo is-before" style="height:150px" role="img" aria-label="Photo of a house before renovation"></div>
    <figcaption class="snap-label" style="padding-left:60px">before</figcaption>
  </figure>

  <figure class="snap" style="left:64px;top:408px;width:184px;height:200px;transform:rotate(-2deg)">
    <div class="snap-photo" style="height:150px" role="img" aria-label="Photo of a renovated cottage with deck and garden, after"></div>
    <figcaption class="snap-label">After</figcaption>
  </figure>

  <figure class="snap" style="left:395px;top:402px;width:160px;height:205px;transform:rotate(12deg)">
    <div class="snap-photo is-before" style="height:150px" role="img" aria-label="Photo of a two-storey house and driveway before renovation"></div>
    <figcaption class="snap-label">Before</figcaption>
  </figure>
  <span class="pin red" style="left:488px;top:414px"></span>

  <figure class="snap" style="left:540px;top:388px;width:203px;height:207px;transform:rotate(-3deg)">
    <div class="snap-photo" style="height:152px" role="img" aria-label="Photo of a renovated blue-grey two-storey house, after"></div>
    <figcaption class="snap-label" style="padding-left:50px">After</figcaption>
  </figure>
  <span class="pin red" style="left:644px;top:392px"></span>

  <figure class="snap" style="left:218px;top:620px;width:150px;height:210px;transform:rotate(14deg)">
    <div class="snap-photo is-before" style="height:152px" role="img" aria-label="Photo of a raised timber house before renovation"></div>
    <figcaption class="snap-label">Before</figcaption>
  </figure>
  <span class="pin green" style="left:306px;top:630px"></span>

  <figure class="snap" style="left:331px;top:612px;width:199px;height:205px;transform:rotate(-3deg)">
    <div class="snap-photo" style="height:152px" role="img" aria-label="Photo of a renovated grey raised cottage with lawn, after"></div>
    <figcaption class="snap-label" style="padding-left:60px">After</figcaption>
  </figure>
  <span class="pin red" style="left:418px;top:614px"></span>

  <p class="tagline">
    <span class="tagline-lead">THE RELIABLE WAY TO EARN</span>
    <span class="tagline-key">HUGE GAINS</span>
    <span class="tagline-tail">FROM BUDGET HOME UPGRADES!</span>
  </p>

  <p class="credits">Created and written by Mara Ellison<br>Ellison Dwellings + Fix It Forward</p>
</div>
</body>
</html>
```